A new website for Electrical Contractor Business

We are looking for a unique and new WordPress website design which would include 5 Pages - Home Page, Meet the Team, Our Services, Our Projects and Contact Us page.

The global theme for the website needs to be professional but simple to navigate as we cater for both business and home owner customers.

Our core business service is targeted around lighting from single room decorative to large office so the theme should incorporate this in some way.

The home page should include;
Our business logo, Contact number, Email address, small Image rotation box - Highlighting pervious projectsText box - With welcome message, chirpnet feed news reel/Customer feed back box.

I would also like to see a 2 boxes for the separate customer types we services. Business and Home Owner. each box will have a small image with a small text description with a link to the area of the services page relevant to that customer type.

Meet the team page -This will be introducing potential customers to the team so I would like it to include for each team member. Something like a small image and text area which will introduce an outline of the team members skills and abilities.

Our Services page This page will be outlining the different services on offer to the both customer types business and homeowner. Each service should have an image with text description of the service would good here.

Our projects page-Will include images of pervious projects and work we have completed along with a text area for the project description/ outliner.

Contact Us page - Should include a contact form which should include an option for the customer to quest us to call them back, also a selection box for them to inform us our how they found our details would be good.

Colour - The theme colours can be taken from the logo or feel free to impress with your own imagination.

Remember we are looking for a website that will interest our customers enough to except our services or be drawn further into the website.. So call to action links to other areas of the site/ contact page are welcome

Target Market(s)

Business - Office, warehousing and Large Store - lighting and Power
Home owner lighting and power

Coding

Coded - Design and coding required

Number of Pages Required

5+ page

Font styles to use
Serif
Sans Serif

Colors

Designer to choose colors to be used in the design.

Requirements
Must have
• Logo integrated into the website design - i.e. website colours which allow the logo to blend into the design.
Nice to have
• Custom but professional theme catering to business customers, but also show that we do provide services to home owners too.
Should not have
• Sorry am not interested in one oversized block image on rotation covering half the home page.. Images will be needed but not a single block over sized frame with not text, shape. Please use your imagination when considering this design

```html
<!DOCTYPE html>
<html lang="en">
<head>
<meta charset="utf-8">
<title>Brightwire Electrical — Lighting Services</title>
<link href="https://fonts.googleapis.com/css2?family=Montserrat:wght@400;500;600;700&family=Open+Sans:ital,wght@0,400;0,600;0,700;1,400&family=Roboto:wght@300;400&display=swap" rel="stylesheet">
<style>
:root{
  --navy:#1f3868;
  --navy-deep:#182d56;
  --orange:#f26a21;
  --sky:#2aa6de;
  --ink:#2b2b2b;
  --muted:#777d87;
  --pale:#f1f4fa;
  --white:#ffffff;
}
*{box-sizing:border-box;margin:0;padding:0}
html,body{width:1200px;height:4775px;overflow:hidden}
body{position:relative;background:var(--white);font-family:"Open Sans",Arial,sans-serif;color:var(--ink)}
.abs{position:absolute}
.btn{position:absolute;display:flex;align-items:center;justify-content:center;border-radius:16px;height:32px;padding:0 24px;font-family:"Montserrat",sans-serif;font-size:11px;font-weight:600;letter-spacing:.5px;color:var(--white);text-transform:uppercase}
.btn--orange{background:var(--orange)}
.btn--navy{background:var(--navy)}
.section-title{position:absolute;left:0;width:1200px;text-align:center;font-family:"Montserrat",sans-serif;font-size:28px;font-weight:500;letter-spacing:1px;color:var(--navy)}
.section-title em{font-style:normal;font-weight:700;color:var(--orange)}
.bolt{position:absolute;left:592px;width:16px;height:20px}
.photo{position:absolute}

/* header */
.site-header{position:absolute;left:0;top:0;width:1200px;height:125px;background:var(--white)}
.brand{position:absolute;left:80px;top:48px;display:flex;align-items:center;gap:10px;font-family:"Montserrat",sans-serif;font-weight:700;font-size:22px;color:var(--navy);letter-spacing:1px}
.brand .dot{width:34px;height:34px;border-radius:50%;background:var(--orange)}
.call{position:absolute;left:764px;top:36px;font-family:"Montserrat",sans-serif;font-size:14px;font-weight:600;color:var(--navy)}
.call b{color:var(--orange)}
.social{position:absolute;top:26px;display:flex;gap:8px}
.social span{width:34px;height:34px;border-radius:50%;background:var(--navy)}
.social span:first-child{background:var(--orange)}
.nav{position:absolute;top:92px;left:0;width:1200px;font-family:"Montserrat",sans-serif;font-size:12px;font-weight:700;color:var(--navy)}
.nav a{position:absolute;text-decoration:none;color:inherit}
.nav a.active{color:var(--orange)}
.nav a.active:before{content:"";position:absolute;left:50%;top:-22px;width:2px;height:12px;background:var(--orange)}

/* hero */
.hero{position:absolute;left:0;top:125px;width:1200px;height:480px;border-bottom-right-radius:180px;overflow:hidden;background:linear-gradient(100deg,#2c231d 0%,#5a4636 40%,#8a7058 62%,#3d3a3a 100%)}
.hero h1{position:absolute;left:76px;top:160px;width:600px;font-family:"Montserrat",sans-serif;font-size:38px;line-height:48px;font-weight:700;color:var(--white)}

/* welcome */
.welcome{position:absolute;left:0;top:605px;width:1200px;height:455px;background:var(--pale)}
.welcome .ring{position:absolute;left:80px;top:80px;width:335px;height:335px;border-radius:50%;border:6px solid var(--navy);padding:8px;background:var(--white)}
.welcome .ring div{width:100%;height:100%;border-radius:50%;background:linear-gradient(135deg,#d9d2c7,#8b7a66 55%,#4d4038)}
.welcome small{position:absolute;left:465px;top:118px;font-family:"Montserrat",sans-serif;font-size:11px;letter-spacing:1px;color:var(--navy)}
.welcome h2{position:absolute;left:465px;top:134px;font-family:"Montserrat",sans-serif;font-size:24px;font-weight:500;letter-spacing:1px;color:var(--navy)}
.welcome h2 em{font-style:normal;font-weight:700;color:var(--orange)}
.welcome p{position:absolute;left:465px;top:180px;width:655px;font-size:13.5px;line-height:24px;color:var(--muted)}

/* services */
.services-band{position:absolute;left:0;top:1385px;width:1200px;height:540px;background:linear-gradient(90deg,#3a3836,#6b6560 45%,#9a8f84 70%,#4a4541)}
.diamond-text{position:absolute;text-align:center;color:var(--white)}
.diamond-text h3{font-family:"Montserrat",sans-serif;font-size:20px;font-weight:700}
.diamond-text p{font-size:12px;line-height:17px;margin-top:6px}
.callout{position:absolute;left:0;width:1200px;text-align:center;color:var(--white)}
.callout .name{top:1565px;font-family:"Montserrat",sans-serif;font-weight:700;font-size:20px;letter-spacing:2px}
.callout .line{font-family:"Roboto",sans-serif;font-weight:300;font-size:34px}
.callout .phone{font-family:"Roboto",sans-serif;font-weight:400;font-size:40px;color:var(--orange);letter-spacing:1px}

/* team */
.member{position:absolute;top:2130px;width:220px;text-align:center}
.member .ring{width:180px;height:180px;margin:0 auto;border-radius:50%;border:5px solid var(--navy);padding:6px;background:var(--white)}
.member .ring div{width:100%;height:100%;border-radius:50%;background:linear-gradient(160deg,#e9e6e2,#b7aea6)}
.member h4{margin-top:18px;font-family:"Montserrat",sans-serif;font-size:13px;font-weight:700;color:var(--navy)}
.member span{font-size:11px;color:var(--muted)}
.member--lead .ring{border-color:var(--orange)}
.member--lead h4{color:var(--orange)}

/* projects */
.projects{position:absolute;left:0;top:2500px;width:1200px;height:667px;background:var(--navy)}
.project-caption{position:absolute;left:380px;top:2895px;color:var(--white)}
.project-caption h3{font-family:"Montserrat",sans-serif;font-size:18px;font-weight:700}
.project-caption p{font-size:12px;line-height:16px;margin-top:6px;width:330px}
.arrow{position:absolute;width:30px;height:30px;border-radius:50%;display:flex;align-items:center;justify-content:center}

/* feedback */
.feedback-title{position:absolute;left:78px;top:3265px;font-family:"Montserrat",sans-serif;font-size:28px;font-weight:500;letter-spacing:1px;color:var(--navy)}
.feedback-title em{font-style:normal;font-weight:700;color:var(--orange)}
.feedback-title:after{content:"";position:absolute;left:100%;margin-left:20px;top:16px;width:70px;height:1px;background:#c8ccd4;box-shadow:0 5px 0 #c8ccd4}
.client{position:absolute;left:80px;top:3335px;width:90px;height:90px;border-radius:50%;border:4px solid var(--navy);padding:4px;background:var(--white)}
.client div{width:100%;height:100%;border-radius:50%;background:linear-gradient(160deg,#e5e1dc,#a99e95)}
.client-name{position:absolute;left:200px;top:3360px;font-family:"Montserrat",sans-serif;font-size:13px;font-weight:700;color:var(--navy)}
.client-role{position:absolute;left:200px;top:3380px;font-size:11px;color:var(--muted)}
.quote{position:absolute;left:80px;top:3445px;width:560px;font-size:13.5px;line-height:22px;font-style:italic;color:var(--muted)}
.stars{position:absolute;left:80px;top:3553px;color:var(--orange);font-size:16px;letter-spacing:2px}
.feed{position:absolute;left:732px;top:3253px;width:398px;height:440px;background:#eef1f6}
.feed-head{height:48px;background:var(--sky);display:flex;align-items:center;justify-content:space-between;padding:0 22px;font-family:"Montserrat",sans-serif;font-weight:700;font-size:17px;color:var(--white)}
.feed-head span{width:22px;height:22px;border-radius:4px;background:var(--white)}
.post{position:absolute;left:25px;width:350px}
.post .ico{position:absolute;left:0;top:6px;width:30px;height:30px;border-radius:4px;background:var(--sky)}
.post .body{margin-left:48px;font-size:11px;line-height:16px;color:var(--muted)}
.post .body b{color:var(--navy);font-family:"Montserrat",sans-serif}
.post .link{display:block;text-align:right;color:var(--sky);font-size:11px;margin-top:4px}

/* news */
.news{position:absolute;left:0;top:3710px;width:1200px;height:650px;background:var(--white)}
.card{position:absolute;top:3877px;width:328px;height:262px;background:var(--pale);text-align:center}
.card .photo{position:relative;height:160px}
.card h4{margin:16px 20px 0;font-family:"Open Sans",sans-serif;font-size:15px;line-height:20px;font-weight:600;color:var(--ink)}
.card h4.under{text-decoration:underline}
.card time{display:block;margin-top:14px;font-size:11px;color:var(--orange)}

/* footer */
.footer{position:absolute;left:0;top:4360px;width:1200px;height:415px;background:var(--navy)}
.footer .brand{left:80px;top:70px;color:var(--white)}
.f-call{position:absolute;left:80px;top:150px;font-family:"Montserrat",sans-serif;font-size:18px;font-weight:600;color:var(--white)}
.f-line{position:absolute;left:80px;font-size:12px;line-height:18px;color:#c7d0e2}
.f-social{position:absolute;left:80px;top:288px;display:flex;gap:8px}
.f-social span{width:30px;height:30px;border-radius:50%;border:1px solid #6d80a8}
.f-social span:first-child{background:var(--orange);border-color:var(--orange)}
.f-head{position:absolute;top:80px;font-family:"Montserrat",sans-serif;font-size:15px;font-weight:600;color:var(--white)}
.links{position:absolute;left:415px;top:120px;list-style:none;font-size:12px;line-height:24px;color:#c7d0e2}
.links li:first-child{color:var(--orange)}
.field{position:absolute;height:30px;border:1px solid #4e6594;background:#2a4577;font-size:11px;color:#c7d0e2;padding:7px 10px}
.f-bottom{position:absolute;top:4715px;font-size:11px;color:#aab6cf}
</style>
</head>
<body>

<header class="site-header">
  <div class="brand"><span class="dot"></span>BRIGHTWIRE</div>
  <div class="call">Call Us : <b>123-456-7890</b></div>
  <div class="social" style="left:985px"><span></span><span></span><span></span></div>
  <nav class="nav">
    <a class="active" style="left:515px">HOME</a>
    <a style="left:612px">SERVICES</a>
    <a style="left:742px">PROJECTS</a>
    <a style="left:866px">MEET THE TEAM</a>
    <a style="left:1035px">CONTACT US</a>
  </nav>
</header>

<section class="hero" role="img" aria-label="Warmly lit modern living room with stone wall and fireplace">
  <h1>Exceptional house and office lighting services</h1>
  <span class="btn btn--orange" style="left:76px;top:275px">Get a free quote</span>
</section>

<section class="welcome">
  <div class="ring"><div role="img" aria-label="Bright modern lounge interior with lighting"></div></div>
  <small>WELCOME TO</small>
  <h2>BRIGHTWIRE <em>SOLUTION</em></h2>
  <p>There are many variations of passages of Lorem Ipsum available, but the majority have suffered alteration in some form, by injected humour, or randomised words which don't look even slightly believable. If you are going to use a passage of Lorem Ipsum, you need to be sure there isn't anything embarrassing hidden in the middle of text. All the Lorem Ipsum generators on the Internet tend.</p>
  <span class="btn btn--navy" style="left:465px;top:360px">Contact us</span>
</section>

<h2 class="section-title" style="top:1105px">OUR <em>SERVICES</em></h2>
<svg class="bolt" style="top:1150px" viewBox="0 0 16 20"><polygon points="9,0 2,11 7,11 5,20 14,8 9,8" fill="#f26a21"/></svg>

<div class="services-band" role="img" aria-label="Dim corridor lit by wall lights"></div>
<svg class="abs" style="left:0;top:1130px" width="1200" height="480" viewBox="0 1130 1200 480">
  <defs>
    <linearGradient id="homeTone" x1="0" y1="0" x2="0" y2="1"><stop offset="0" stop-color="#5b6d8f"/><stop offset="1" stop-color="#2d3448"/></linearGradient>
    <linearGradient id="officeTone" x1="0" y1="0" x2="0" y2="1"><stop offset="0" stop-color="#f58a45"/><stop offset="1" stop-color="#e9621a"/></linearGradient>
  </defs>
  <polygon points="372,1140 602,1370 372,1600 142,1370" fill="url(#homeTone)" role="img" aria-label="Home decorative lighting interior"/>
  <polygon points="827,1140 1057,1370 827,1600 597,1370" fill="url(#officeTone)" role="img" aria-label="Office decorative lighting interior"/>
</svg>
<div class="diamond-text" style="left:232px;top:1340px;width:280px">
  <h3>Home Decorative</h3>
  <p>Lorem ipsum dolor sit amet, consectetur adipiscing elit, sed do eiusmod tempor.</p>
</div>
<div class="diamond-text" style="left:687px;top:1312px;width:280px">
  <h3>Office Decorative</h3>
  <p>Lorem ipsum dolor sit amet, consectetur adipiscing elit, sed do eiusmod tempor.</p>
</div>
<span class="btn btn--navy" style="left:777px;top:1415px;height:28px">Read more</span>

<div class="callout name">BRIGHTWIRE</div>
<div class="callout line" style="top:1682px">One Call Can Solve All your Light Problem</div>
<div class="callout phone" style="top:1730px">123-456-7890</div>
<span class="btn" style="left:548px;top:1818px;background:var(--white);color:var(--navy)">Contact us</span>

<h2 class="section-title" style="top:2005px">MEET THE <em style="color:var(--orange)">TEAM</em></h2>
<svg class="bolt" style="top:2050px" viewBox="0 0 16 20"><polygon points="9,0 2,11 7,11 5,20 14,8 9,8" fill="#f26a21"/></svg>
<div class="member" style="left:103px"><div class="ring"><div role="img" aria-label="Team member portrait"></div></div><h4>STANDARD CHUNK</h4><span>Simply Dummy</span></div>
<div class="member" style="left:361px"><div class="ring"><div role="img" aria-label="Team member portrait"></div></div><h4>FINIBUS BONORUM</h4><span>Simply Dummy</span></div>
<div class="member member--lead" style="left:622px"><div class="ring"><div role="img" aria-label="Team member portrait"></div></div><h4>STANDARD CHUNK</h4><span>Simply Dummy</span></div>
<div class="member" style="left:886px"><div class="ring"><div role="img" aria-label="Team member portrait"></div></div><h4>FINIBUS BONORUM</h4><span>Simply Dummy</span></div>
<span class="btn btn--navy" style="left:535px;top:2398px">View all team</span>

<section class="projects"></section>
<h2 class="section-title" style="top:2585px;color:var(--white)">OUR <em>PROJECTS</em></h2>
<svg class="bolt" style="top:2630px" viewBox="0 0 16 20"><polygon points="9,0 2,11 7,11 5,20 14,8 9,8" fill="#f26a21"/></svg>
<div class="photo" style="left:0;top:2690px;width:318px;height:318px;background:linear-gradient(135deg,#bfb3a4,#5d4d40)" role="img" aria-label="Living room project with fireplace"></div>
<div class="photo" style="left:350px;top:2690px;width:503px;height:318px;background:linear-gradient(160deg,#e2dcd3,#8d7d6d 55%,#3f3a3a)" role="img" aria-label="Open plan home with ceiling downlights"></div>
<div class="photo" style="left:885px;top:2690px;width:315px;height:318px;background:linear-gradient(135deg,#c9b48e,#7a6242)" role="img" aria-label="Office floor with panel lighting"></div>
<div class="project-caption"><h3>Home Decorative</h3><p>There are many variations of passages of Lorem Ipsum available, but the majority have suffered.</p></div>
<div class="arrow" style="left:335px;top:2835px;background:var(--white)"><svg width="10" height="12" viewBox="0 0 10 12"><polyline points="7,1 2,6 7,11" fill="none" stroke="#1f3868" stroke-width="2"/></svg></div>
<div class="arrow" style="left:838px;top:2835px;background:var(--orange)"><svg width="10" height="12" viewBox="0 0 10 12"><polyline points="3,1 8,6 3,11" fill="none" stroke="#fff" stroke-width="2"/></svg></div>
<span class="btn btn--orange" style="left:520px;top:3065px">View all projects</span>

<h2 class="feedback-title">CUSTOMER <em>FEEDBACK</em></h2>
<div class="client"><div role="img" aria-label="Customer portrait"></div></div>
<div class="client-name">STANDARD CHUNK</div>
<div class="client-role">Simply Dummy</div>
<p class="quote">"But I must explain to you how all this mistaken idea of denouncing pleasure and praising pain was born and I will give you a complete account of the system, and expound the actual teachings of the great explorer of the truth, the master-builder of human happiness..."</p>
<div class="stars">★★★★☆</div>
<span class="btn btn--orange" style="left:80px;top:3630px">View all feedback</span>

<aside class="feed">
  <div class="feed-head">chirpnet<span></span></div>
  <div class="post" style="top:72px"><span class="ico"></span><div class="body"><b>chirpnet</b> – 22 April 2019<br>Contrary to popular belief, Lorem Ipsum is not simply random text. It has roots in a piece of classical Latin literature from.<span class="link">View on chirpnet</span></div></div>
  <div class="post" style="top:198px"><span class="ico"></span><div class="body"><b>chirpnet</b> – 22 April 2019<br>Contrary to popular belief, Lorem Ipsum is not simply random text. It has roots in a piece of classical Latin literature from.<span class="link">View on chirpnet</span></div></div>
  <div class="post" style="top:324px"><span class="ico"></span><div class="body"><b>chirpnet</b> – 22 April 2019<br>Contrary to popular belief, Lorem Ipsum is not simply random text. It has roots in a piece of classical Latin literature from.<span class="link">View on chirpnet</span></div></div>
</aside>

<section class="news"></section>
<h2 class="section-title" style="top:3772px">LATEST <em>NEWS</em></h2>
<svg class="bolt" style="top:3817px" viewBox="0 0 16 20"><polygon points="9,0 2,11 7,11 5,20 14,8 9,8" fill="#f26a21"/></svg>
<article class="card" style="left:80px"><div class="photo" style="background:linear-gradient(135deg,#c8beb2,#6e5d4e)" role="img" aria-label="Lit stone-wall living room"></div><h4>Lorem ipsum dolor sit amet, consectetur adipiscing elit, sed eiusmod tempor</h4><time>22 April 2019</time></article>
<article class="card" style="left:436px"><div class="photo" style="background:linear-gradient(135deg,#e3ddd4,#9a8570)" role="img" aria-label="Bright kitchen and dining area"></div><h4 class="under">Lorem ipsum dolor sit amet, consectetur adipiscing elit, sed eiusmod tempor</h4><time>22 April 2019</time></article>
<article class="card" style="left:792px"><div class="photo" style="background:linear-gradient(135deg,#d7d6d4,#7d7c7c)" role="img" aria-label="Reception area with feature lighting"></div><h4>Lorem ipsum dolor sit amet, consectetur adipiscing elit, sed eiusmod tempor</h4><time>22 April 2019</time></article>
<span class="btn btn--navy" style="left:522px;top:4245px">View all news</span>

<footer class="footer">
  <div class="brand"><span class="dot"></span>BRIGHTWIRE</div>
  <div class="f-call">Call: +123 - 456 - 7890</div>
  <div class="f-line" style="top:180px">hello@brightwire-electric.com</div>
  <div class="f-line" style="top:215px">48 Lantern Row, Fairhaven,<br>FH 20418</div>
  <div class="f-social"><span></span><span></span><span></span></div>
  <div class="f-head" style="left:415px">Quick Links</div>
  <ul class="links"><li>Home</li><li>Services</li><li>Projects</li><li>Meet The Team</li><li>Contact Us</li></ul>
  <div class="f-head" style="left:592px">Send Us a Message</div>
  <svg class="abs" style="left:1102px;top:80px" width="22" height="20" viewBox="0 0 22 20"><polygon points="11,1 21,19 1,19" fill="none" stroke="#f26a21" stroke-width="2"/><line x1="11" y1="8" x2="11" y2="13" stroke="#f26a21" stroke-width="2"/><circle cx="11" cy="16" r="1.2" fill="#f26a21"/></svg>
  <div class="field" style="left:592px;top:120px;width:165px">Name</div>
  <div class="field" style="left:774px;top:120px;width:165px">Phone</div>
  <div class="field" style="left:956px;top:120px;width:165px">Email</div>
  <div class="field" style="left:592px;top:165px;width:529px;height:105px">Message ...</div>
  <div class="arrow" style="left:1061px;top:275px;background:var(--orange)"><svg width="10" height="12" viewBox="0 0 10 12"><polyline points="3,1 8,6 3,11" fill="none" stroke="#fff" stroke-width="2"/></svg></div>
</footer>
<div class="f-bottom" style="left:80px">© 2019 Brightwire Electrical. All Rights Reserved</div>
<div class="f-bottom" style="left:592px">Privacy Policy &nbsp; | &nbsp; Terms &amp; Conditions</div>

</body>
</html>
```